Business Card for Makeup Artist

I need a business card designed for my makeup and hair artistry business which is primarily events and weddings focused. The card needs to be sleek, simple, stylish and appealing to women. I would prefer a white background but open to suggestions also. I also love the marble background look. I have attached some example pics. It needs to be a double sided card with logo and/or design on one side and contact details in the centre of the card on the other side. NO LOGO ON BACK. Examples attached.

Target Market(s)

Females age 14-55

Industry/Entity Type

Business

Contact Information for Business Card

Nora Vint
Principal Makeup Artist
P: 0413 925 214
E: nora@lumirabeauty.com.au
W: www.lumirabeauty.com.au

Requirements
Should not have
• No yellow, green, red or blue in the design.

```html
<!DOCTYPE html>
<html lang="en">
<head>
<meta charset="utf-8">
<title>Lumira Makeup Artistry – Business Card</title>
<link href="https://fonts.googleapis.com/css2?family=Arimo:wght@400;700&display=swap" rel="stylesheet">
<style>
  :root {
    --backdrop: #ecebea;
    --card-white: #ffffff;
    --brand-pink: #de85bd;
    --brand-grey: #777777;
    --rule-grey: #8a8a8a;
    --ink: #1e1e1e;
    --font-main: "Arimo", Arial, sans-serif;
  }
  * { box-sizing: border-box; margin: 0; padding: 0; }
  html, body {
    width: 1200px; height: 864px; overflow: hidden;
    background: var(--backdrop);
    font-family: var(--font-main);
  }
  .canvas {
    position: relative; width: 1200px; height: 864px;
  }
  .card {
    position: absolute; top: 277px;
    width: 540px; height: 310px;
    box-shadow: 0 6px 18px rgba(0,0,0,0.12);
    overflow: hidden;
  }
  .card--front { left: 40px; background: var(--card-white); }
  .card--back  { left: 620px; background: var(--brand-pink); }

  /* brand name */
  .brand { color: var(--brand-grey); font-weight: 400; }
  .brand__name { display: block; line-height: 1; }
  .brand__tag {
    display: block; text-transform: uppercase;
    letter-spacing: 0.04em; line-height: 1;
  }
  .card--front .brand { position: absolute; left: 34px; top: 38px; }
  .card--front .brand__name { font-size: 56px; }
  .card--front .brand__tag { font-size: 19px; margin-top: 6px; margin-left: 18px; }

  .card--back .brand { position: absolute; left: 0; right: 0; top: 92px; text-align: center; }
  .card--back .brand__name { font-size: 84px; }
  .card--back .brand__tag { font-size: 27px; margin-top: 10px; margin-left: 60px; }

  /* front layout */
  .divider {
    position: absolute; left: 303px; top: 44px; width: 1px; height: 182px;
    background: var(--rule-grey);
  }
  .rule {
    position: absolute; left: 0; right: 0; top: 227px; height: 1px;
    background: var(--rule-grey);
  }
  .band {
    position: absolute; left: 0; right: 0; top: 233px; height: 46px;
    background: var(--brand-pink);
  }
  .contact {
    position: absolute; left: 320px; top: 126px;
    color: var(--ink);
  }
  .contact__name { color: var(--brand-pink); font-size: 19px; line-height: 1.05; }
  .contact__role { font-size: 14px; margin-bottom: 8px; }
  .contact__list { list-style: none; }
  .contact__item {
    display: flex; align-items: center; gap: 8px;
    font-size: 13.5px; line-height: 1; margin-bottom: 4px;
  }
  .contact__item--plain { padding-left: 0; }
  .icon { width: 15px; height: 15px; flex: none; }
</style>
</head>
<body>
<main class="canvas">

  <section class="card card--front" aria-label="Business card front">
    <div class="brand">
      <span class="brand__name">Lumira</span>
      <span class="brand__tag">Makeup Artistry</span>
    </div>
    <div class="divider"></div>
    <div class="contact">
      <p class="contact__name">Nora Vint</p>
      <p class="contact__role">Principal Makeup Artist</p>
      <ul class="contact__list">
        <li class="contact__item">
          <svg class="icon" viewBox="0 0 16 16" aria-hidden="true">
            <rect width="16" height="16" fill="#de85bd"/>
            <path d="M5 3.5l1.8 2.2-1 1.2c.6 1.4 1.6 2.5 3 3.1l1.2-1 2.2 1.8-1 1.6C8 12 4.2 8.4 3.6 4.5z" fill="#fff"/>
          </svg>
          0413 925 214
        </li>
        <li class="contact__item">
          <svg class="icon" viewBox="0 0 16 16" aria-hidden="true">
            <rect width="16" height="16" fill="#de85bd"/>
            <rect x="3" y="4.5" width="10" height="7" fill="none" stroke="#fff" stroke-width="1.2"/>
            <path d="M3 4.5l5 4 5-4" fill="none" stroke="#fff" stroke-width="1.2"/>
          </svg>
          nora@lumirabeauty.com.au
        </li>
        <li class="contact__item">
          <svg class="icon" viewBox="0 0 16 16" aria-hidden="true">
            <rect width="16" height="16" fill="#de85bd"/>
            <circle cx="8" cy="8" r="4.8" fill="none" stroke="#fff" stroke-width="1.2"/>
            <path d="M3.2 8h9.6M8 3.2c-2 2.6-2 7 0 9.6M8 3.2c2 2.6 2 7 0 9.6" fill="none" stroke="#fff" stroke-width="1"/>
          </svg>
          www.lumirabeauty.com.au
        </li>
      </ul>
    </div>
    <div class="rule"></div>
    <div class="band"></div>
  </section>

  <section class="card card--back" aria-label="Business card back">
    <div class="brand">
      <span class="brand__name">Lumira</span>
      <span class="brand__tag">Makeup Artistry</span>
    </div>
  </section>

</main>
</body>
</html>
```